Presentation Template for Copperleaf Studio

We would like to have a template for our presentations since we have a new logo and want a new general image.

The new template should have as minimum Cover/Title Page, Bullets page and Regular page. We have a new logo and need the template to mach with it. For the bullets and regular page we want the design no take much part for including content, so we would like something that makes the slides look good but leaving most of room free for writing.

We would like the logo on the footer of the regular slides (not of course for the cover, dividers etc)

I'm attaching de logo here. Our logo colours are #b80016, #006ac6 and black

Thank you

Industry/Entity Type

It Company

Font styles to use
Other font styles liked:
• Maven Pro

Colors
ec1f27
0355a3
000000

Requirements
Must have
• Presentation template with Cover/Title Page, Bullets page and Regular page. Must match with our new logo.
• We would like the logo on the footer of the regular slides (not of course for the cover, dividers etc)
• Our logo colours are #b80016, #006ac6 and black
Nice to have
• Other type of slides, special bullets etc
Should not have
• I don't know

```html
<!DOCTYPE html>
<html lang="en">
<head>
<meta charset="utf-8">
<title>Copperleaf Studio – Presentation Template</title>
<link href="https://fonts.googleapis.com/css2?family=Open+Sans:ital,wght@0,400;0,600;0,700;1,400;1,600&family=Maven+Pro:wght@500;600&display=swap" rel="stylesheet">
<style>
:root{
  --red:#c8102e;
  --red-deep:#9e0b1f;
  --red-bright:#e0202e;
  --pink:#d9868f;
  --blue:#0355a3;
  --ink:#222;
  --grey:#8a8a8a;
  --board:#2b2b2b;
  --white:#fff;
}
*{box-sizing:border-box;margin:0;padding:0}
html,body{width:1200px;height:893px;overflow:hidden;background:var(--board)}
body{position:relative;font-family:"Open Sans",Arial,sans-serif;color:var(--ink)}
.slide{position:absolute;width:288px;height:168px;background:var(--white);overflow:hidden}
.pg{position:absolute;right:6px;bottom:4px;width:9px;height:7px;background:var(--blue);color:#fff;font-size:4px;line-height:7px;text-align:center;font-weight:600}
.brand{position:absolute;left:12px;top:8px;display:flex;align-items:center;gap:3px}
.brand-mark{width:9px;height:9px;background:var(--red)}
.brand-name{font-size:5.2px;line-height:5.4px;font-weight:700;color:var(--red);letter-spacing:.4px}
.brand.on-red .brand-mark{background:#fff}
.brand.on-red .brand-name{color:#fff}
.brand.right{left:auto;right:12px}
.head{position:absolute;font-size:5px;font-weight:700;color:var(--red)}
.body{position:absolute;font-size:4px;line-height:5.6px;color:var(--grey)}
.title{position:absolute;font-size:10px;line-height:12.5px;font-weight:700;color:var(--red)}
.title.small{font-size:9px;line-height:11.5px}
.photo{position:absolute}
.ph-blue{background:linear-gradient(135deg,#1d4f7a,#7fb4d6 55%,#2a3e55)}
.ph-suit{background:linear-gradient(135deg,#5d6670,#a3acb5 50%,#3c434a)}
.ph-red{background:linear-gradient(135deg,#a30d1e,#d63a44 50%,#8c0a19)}
.ph-light{background:linear-gradient(135deg,#e6e9ee,#c9ced6 50%,#eef0f3)}
.bullet{position:absolute;display:flex;align-items:center;gap:5px;font-size:4px;color:var(--grey)}
.dot{width:10px;height:10px;border-radius:50%;background:var(--red);color:#fff;font-size:4px;font-weight:700;display:flex;align-items:center;justify-content:center;flex:none}
.dot.d2{background:var(--red-deep)}
.dot.d3{background:var(--pink)}
.white{color:#fff}
.italic{font-style:italic}
.cover-name{font-family:"Maven Pro",sans-serif;color:#fff}
.cover-name .line{font-size:23px;font-weight:600;letter-spacing:2px;line-height:25px}
.cover-name .sub{font-family:"Open Sans",sans-serif;font-size:9px;font-weight:400;margin-top:5px}
</style>
</head>
<body>

<!-- Profile -->
<section class="slide" style="left:10px;top:10px">
  <div class="brand"><span class="brand-mark"></span><span class="brand-name">COPPERLEAF<br>STUDIO</span></div>
  <div class="head" style="left:12px;top:44px">About Profile</div>
  <p class="body" style="left:12px;top:53px;width:62px;font-size:3.6px;line-height:5px">Cloud services built to scale with your team. We plan, build and run secure systems so people can focus on the work that matters most. Our team supports every step from the first idea to daily use and long term growth across every office.</p>
  <div class="photo ph-suit" style="left:78px;top:26px;width:102px;height:142px" role="img" aria-label="Portrait of a team member in a suit"></div>
  <div style="position:absolute;left:180px;top:0;width:108px;height:168px;background:var(--red)"></div>
  <div class="white" style="position:absolute;left:200px;top:30px;font-size:5px;font-weight:600">Employee Name</div>
  <div class="white" style="position:absolute;left:200px;top:66px;font-size:11px;font-weight:700">Who I’m?</div>
  <p class="body white italic" style="left:200px;top:86px;width:66px">Short profile text about this person, their role, skills and the cloud projects they lead for clients every day.</p>
  <div class="pg">02</div>
</section>

<!-- Triangle infographic -->
<section class="slide" style="left:308px;top:10px">
  <div class="brand"><span class="brand-mark"></span><span class="brand-name">COPPERLEAF<br>STUDIO</span></div>
  <div class="title" style="left:14px;top:58px">Triangle<br>Shape in<br>Inforgraphics</div>
  <p class="body" style="left:14px;top:100px;width:64px">Short body text for this slide with room for a clear idea.</p>
  <svg style="position:absolute;left:76px;top:30px" width="124" height="116" viewBox="0 0 124 116">
    <polygon points="62,2 92,56 32,56" fill="var(--red)"/>
    <polygon points="62,56 92,56 77,82 47,82 32,56" fill="var(--red-bright)" opacity=".9"/>
    <polygon points="32,56 62,110 2,110" fill="var(--red-bright)"/>
    <polygon points="92,56 122,110 62,110" fill="var(--red-deep)"/>
    <g fill="#fff" font-size="4.4" font-weight="700" font-family="Open Sans,sans-serif" text-anchor="middle">
      <text x="62" y="44">Triangle 1</text><text x="62" y="70">Triangle 2</text>
      <text x="32" y="94">Triangle 3</text><text x="92" y="94">Triangle 4</text>
    </g>
  </svg>
  <div class="head" style="left:206px;top:40px">About Graph Head</div>
  <p class="body" style="left:206px;top:48px;width:70px">Short text to explain each part of the graph and what it means for the plan ahead.</p>
  <div class="pg">02</div>
</section>

<!-- Circle infographic -->
<section class="slide" style="left:604px;top:10px">
  <div class="brand"><span class="brand-mark"></span><span class="brand-name">COPPERLEAF<br>STUDIO</span></div>
  <div class="title" style="left:14px;top:58px">Circle<br>Shape in<br>Inforgraphics</div>
  <p class="body" style="left:14px;top:100px;width:64px">Short body text for this slide with room for a clear idea.</p>
  <div class="photo ph-blue" style="left:110px;top:58px;width:80px;height:80px;border-radius:50%" role="img" aria-label="Hand touching a cloud icon"></div>
  <svg style="position:absolute;left:98px;top:30px" width="140" height="120" viewBox="0 0 140 120">
    <circle cx="52" cy="68" r="44" fill="none" stroke="var(--red)" stroke-width="4"/>
    <line x1="64" y1="20" x2="82" y2="6" stroke="var(--red)" stroke-width="1"/>
    <line x1="82" y1="6" x2="140" y2="6" stroke="var(--red)" stroke-width="1"/>
    <circle cx="62" cy="22" r="5" fill="#fff" stroke="var(--red)" stroke-width="2"/>
  </svg>
  <div class="head" style="left:202px;top:40px">About Circle Head</div>
  <p class="body" style="left:202px;top:48px;width:74px">Short text about the circle and the idea inside it, with space for a few clear lines that keep the slide easy to read.</p>
  <div class="pg">02</div>
</section>

<!-- Section title -->
<section class="slide" style="left:902px;top:10px;background:var(--red)">
  <div class="brand on-red" style="left:88px;top:54px"><span class="brand-mark" style="width:14px;height:14px"></span><span class="brand-name" style="font-size:8px;line-height:8.5px">COPPERLEAF<br>STUDIO</span></div>
  <div class="white" style="position:absolute;left:0;width:288px;top:92px;text-align:center;font-size:14px;font-weight:700">SECTION SLIDE TITLE HERE</div>
  <p class="body white" style="left:50px;top:114px;width:188px;text-align:center;font-size:4.4px">Short line to explain what this section is about and what comes next.</p>
  <div class="pg">02</div>
</section>

<!-- Portfolio grid -->
<section class="slide" style="left:10px;top:190px">
  <div class="brand"><span class="brand-mark"></span><span class="brand-name">COPPERLEAF<br>STUDIO</span></div>
  <div class="head" style="left:20px;top:38px">About Portfolio Head</div>
  <p class="body" style="left:20px;top:47px;width:64px">Short body text about the work shown in the photos with a clear idea.</p>
  <p class="body" style="left:20px;top:105px;width:64px">More text about this project and what it gives the client.</p>
  <div class="photo ph-blue" style="left:96px;top:26px;width:48px;height:36px" role="img" aria-label="Cloud over a glowing hand"></div>
  <div class="photo ph-blue" style="left:146px;top:26px;width:84px;height:36px" role="img" aria-label="Network lights over a business scene"></div>
  <div class="photo ph-suit" style="left:96px;top:64px;width:134px;height:68px" role="img" aria-label="Man in a suit touching a cloud icon"></div>
  <div class="photo ph-suit" style="left:232px;top:26px;width:50px;height:106px" role="img" aria-label="Hands holding a cloud"></div>
  <div class="pg">02</div>
</section>

<!-- Portfolio triangle -->
<section class="slide" style="left:308px;top:190px">
  <div class="brand"><span class="brand-mark"></span><span class="brand-name">COPPERLEAF<br>STUDIO</span></div>
  <div class="head" style="left:20px;top:38px">About Portfolio Head</div>
  <p class="body" style="left:20px;top:47px;width:64px">Short body text about the work shown in the photo with a clear idea.</p>
  <p class="body" style="left:20px;top:105px;width:64px">More text about this project and what it gives the client.</p>
  <svg style="position:absolute;left:112px;top:20px" width="160" height="140" viewBox="0 0 160 140" role="img" aria-label="Hand touching a cloud and device icons, framed in a triangle">
    <defs><linearGradient id="tri" x1="0" y1="0" x2="1" y2="1"><stop offset="0" stop-color="#a3acb5"/><stop offset="1" stop-color="#3c434a"/></linearGradient></defs>
    <polygon points="80,4 158,136 2,136" fill="url(#tri)" stroke="#2a2a2a" stroke-width="3"/>
  </svg>
  <div class="pg">02</div>
</section>

<!-- Section triangle on light photo -->
<section class="slide" style="left:604px;top:190px">
  <div class="photo ph-light" style="left:0;top:0;width:288px;height:168px" role="img" aria-label="Bright server room aisle"></div>
  <div class="brand"><span class="brand-mark"></span><span class="brand-name">COPPERLEAF<br>STUDIO</span></div>
  <svg style="position:absolute;left:88px;top:28px" width="116" height="132" viewBox="0 0 116 132">
    <polygon points="58,2 114,130 2,130" fill="var(--red)" opacity=".92"/>
  </svg>
  <div class="white" style="position:absolute;left:96px;width:100px;top:88px;text-align:center;font-size:4.6px;font-weight:700;line-height:6px">About<br>Section Head</div>
  <p class="body white" style="left:118px;top:104px;width:56px;text-align:center">Short text about this section and the main idea behind it.</p>
  <div class="pg">02</div>
</section>

<!-- Quote slide -->
<section class="slide" style="left:902px;top:190px">
  <div class="photo ph-red" style="left:0;top:0;width:288px;height:168px" role="img" aria-label="Red tinted business scene"></div>
  <div class="brand on-red"><span class="brand-mark"></span><span class="brand-name">COPPERLEAF<br>STUDIO</span></div>
  <p class="white italic" style="position:absolute;left:26px;top:96px;width:190px;font-size:8px;line-height:12px">Cloud services that grow with your team, built with care and run with calm every day.</p>
  <div class="pg">02</div>
</section>

<!-- Cover -->
<section class="slide" style="left:8px;top:364px;width:594px;height:340px">
  <div class="photo ph-red" style="left:0;top:0;width:594px;height:340px" role="img" aria-label="Red tinted hands holding a cloud"></div>
  <div style="position:absolute;left:168px;top:132px;display:flex;align-items:center;gap:12px">
    <span style="width:66px;height:66px;background:#fff"></span>
    <div class="cover-name">
      <div class="line">COPPERLEAF</div>
      <div class="line">STUDIO</div>
      <div class="sub">Cloud services for growing teams</div>
    </div>
  </div>
</section>

<!-- Phone display -->
<section class="slide" style="left:604px;top:364px">
  <div class="brand"><span class="brand-mark"></span><span class="brand-name">COPPERLEAF<br>STUDIO</span></div>
  <div class="title small" style="left:14px;top:64px">PHONE DISPLAY<br>HEAD</div>
  <p class="body" style="left:14px;top:94px;width:64px">Short body text for this slide with room for one idea.</p>
  <div class="photo ph-suit" style="left:104px;top:30px;width:58px;height:138px;border-radius:14px 14px 0 0" role="img" aria-label="Hand holding a smartphone showing an app"></div>
  <div class="head" style="left:186px;top:26px">About Head</div>
  <p class="body" style="left:186px;top:34px;width:92px">Short text to explain the app on screen and what it helps people do.</p>
  <div class="bullet" style="left:186px;top:66px;width:92px"><span class="dot">01</span>Short point about the app and its use.</div>
  <div class="bullet" style="left:186px;top:86px;width:92px"><span class="dot d2">02</span>Short point about the app and its use.</div>
  <div class="bullet" style="left:186px;top:106px;width:92px"><span class="dot">03</span>Short point about the app and its use.</div>
  <div class="pg">02</div>
</section>

<!-- Phone display red circle -->
<section class="slide" style="left:900px;top:364px;width:290px">
  <div style="position:absolute;left:-40px;top:-36px;width:168px;height:190px;border-radius:50%;background:var(--red)"></div>
  <div class="brand on-red" style="left:18px;top:34px"><span class="brand-mark"></span><span class="brand-name">COPPERLEAF<br>STUDIO</span></div>
  <div class="title small white" style="left:14px;top:64px">PHONE DISPLAY<br>HEAD</div>
  <p class="body white" style="left:14px;top:94px;width:64px">Short body text for this slide with room for one idea.</p>
  <div class="brand right"><span class="brand-mark"></span><span class="brand-name">COPPERLEAF<br>STUDIO</span></div>
  <div class="head" style="left:142px;top:26px">About Head</div>
  <p class="body" style="left:142px;top:34px;width:136px">Short text to explain the topic of this slide. Leave most of the room free so the content can breathe and stay clear to read.</p>
  <div class="bullet" style="left:142px;top:76px"><span class="dot">01</span>Short point about this topic.</div>
  <div class="bullet" style="left:142px;top:96px"><span class="dot d2">02</span>Short point about this topic.</div>
  <div class="bullet" style="left:142px;top:116px"><span class="dot d3">03</span>Short point about this topic.</div>
  <div class="pg">02</div>
</section>

<!-- Three column layout -->
<section class="slide" style="left:604px;top:538px">
  <div class="brand"><span class="brand-mark"></span><span class="brand-name">COPPERLEAF<br>STUDIO</span></div>
  <div class="title small" style="left:14px;top:50px">THREE COLOUMN<br>LAYOUT</div>
  <p class="body" style="left:14px;top:80px;width:64px">Short body text for this slide with room for one idea.</p>
  <div class="photo ph-blue" style="left:106px;top:28px;width:56px;height:100px" role="img" aria-label="Hands holding a cloud"></div>
  <div class="photo ph-suit" style="left:166px;top:28px;width:56px;height:100px" role="img" aria-label="Cloud above open hands"></div>
  <div class="photo ph-blue" style="left:226px;top:28px;width:56px;height:100px" role="img" aria-label="Finger touching a cloud icon"></div>
  <p class="body" style="left:106px;top:132px;width:56px">Short caption for this photo</p>
  <p class="body" style="left:166px;top:132px;width:56px">Short caption for this photo</p>
  <p class="body" style="left:226px;top:132px;width:56px">Short caption for this photo</p>
  <div class="pg">02</div>
</section>

<!-- Circle callout -->
<section class="slide" style="left:900px;top:538px;width:290px">
  <div class="photo ph-blue" style="left:-50px;top:-40px;width:190px;height:210px;border-radius:50%" role="img" aria-label="Business person touching a cloud icon"></div>
  <div style="position:absolute;left:60px;top:58px;width:74px;height:74px;border-radius:50%;background:var(--red-bright)"></div>
  <p class="body white" style="left:68px;top:78px;width:58px;text-align:center">Short callout text with one clear key idea for the team.</p>
  <div class="brand right"><span class="brand-mark"></span><span class="brand-name">COPPERLEAF<br>STUDIO</span></div>
  <div class="head" style="left:142px;top:36px">About Head</div>
  <p class="body" style="left:142px;top:44px;width:136px">Short text to explain the topic of this slide with space left for the content.</p>
  <div class="bullet" style="left:142px;top:76px"><span class="dot">01</span>Short point about this topic.</div>
  <div class="bullet" style="left:142px;top:96px"><span class="dot d2">02</span>Short point about this topic.</div>
  <div class="bullet" style="left:142px;top:116px"><span class="dot d3">03</span>Short point about this topic.</div>
  <div class="pg">02</div>
</section>

<!-- Portfolio two blocks -->
<section class="slide" style="left:10px;top:714px">
  <div class="brand"><span class="brand-mark"></span><span class="brand-name">COPPERLEAF<br>STUDIO</span></div>
  <div class="head" style="left:20px;top:38px">About Portfolio Head</div>
  <p class="body" style="left:20px;top:46px;width:118px">Short body text about this project and the result it gave the client over the year.</p>
  <div class="head" style="left:20px;top:104px">About Portfolio Head</div>
  <p class="body" style="left:20px;top:112px;width:118px">Short body text about this project and the result it gave the client over the year.</p>
  <div class="photo ph-suit" style="left:144px;top:30px;width:128px;height:126px" role="img" aria-label="Finger touching a cloud icon"></div>
  <div class="pg">02</div>
</section>

<!-- Products -->
<section class="slide" style="left:304px;top:714px">
  <div style="position:absolute;left:0;top:10px;width:3px;height:12px;background:var(--red)"></div>
  <div class="head" style="left:8px;top:10px;font-size:7px">Our Products</div>
  <div class="brand right" style="top:6px"><span class="brand-mark"></span><span class="brand-name">COPPERLEAF<br>STUDIO</span></div>
  <div class="photo ph-suit" style="left:0;top:28px;width:90px;height:140px" role="img" aria-label="Open hands holding a cloud"></div>
  <div style="position:absolute;left:90px;top:28px;width:114px;height:140px;background:var(--red)"></div>
  <svg style="position:absolute;left:129px;top:44px" width="36" height="36" viewBox="0 0 36 36"><circle cx="18" cy="18" r="16" fill="none" stroke="rgba(255,255,255,.5)" stroke-width="1"/><path d="M18 2 A16 16 0 1 1 2.8 13" fill="none" stroke="#fff" stroke-width="1.5"/><text x="18" y="21" fill="#fff" font-size="8" text-anchor="middle" font-family="Open Sans,sans-serif">80%</text></svg>
  <p class="body white" style="left:98px;top:92px;width:100px">Short text about this product and the value it gives each team.</p>
  <p class="body white" style="left:98px;top:110px;width:100px">Short text about how it runs in the cloud.</p>
  <p class="body white" style="left:98px;top:128px;width:100px">Short text about support and growth.</p>
  <div class="photo ph-blue" style="left:204px;top:28px;width:84px;height:140px" role="img" aria-label="Hand reaching to a glowing cloud"></div>
  <div class="pg">01</div>
</section>

<!-- Partner badges -->
<section class="slide" style="left:604px;top:714px">
  <div class="head" style="left:8px;top:10px;color:var(--ink);font-size:5.5px">Logo Section here</div>
  <div class="brand right" style="top:6px"><span class="brand-mark"></span><span class="brand-name">COPPERLEAF<br>STUDIO</span></div>
  <div style="position:absolute;left:20px;top:40px;width:24px;height:24px;border-radius:50%;background:var(--red)"></div>
  <div style="position:absolute;left:20px;top:84px;width:24px;height:20px;background:var(--blue)"></div>
  <div style="position:absolute;left:18px;top:124px;width:28px;height:14px;background:var(--red)"></div>
  <p class="body" style="left:62px;top:38px;width:96px">Short text about this partner and the work we share together.</p>
  <p class="body" style="left:62px;top:80px;width:96px">Short text about this partner and the work we share together.</p>
  <p class="body" style="left:62px;top:120px;width:96px">Short text about this partner and the work we share together.</p>
  <p class="body" style="left:174px;top:38px;width:104px">Longer text about our partners, how we work with each of them and what this means for our clients in every project we run.</p>
  <p class="body" style="left:174px;top:92px;width:104px">More text on the shared goals and the services we plan to bring next year.</p>
  <div class="pg">01</div>
</section>

<!-- Numbered list -->
<section class="slide" style="left:900px;top:714px;width:290px">
  <div class="photo ph-red" style="left:0;top:0;width:134px;height:168px" role="img" aria-label="Red tinted server racks"></div>
  <p class="white italic" style="position:absolute;left:16px;top:74px;width:108px;font-size:5px;line-height:7.5px">Short quote about our cloud work and the way we help each team grow with calm.</p>
  <div class="brand right"><span class="brand-mark"></span><span class="brand-name">COPPERLEAF<br>STUDIO</span></div>
  <div style="position:absolute;left:140px;top:36px;font-size:8px;color:var(--red)">01</div>
  <div class="head" style="left:156px;top:38px">About One</div>
  <p class="body" style="left:156px;top:46px;width:124px">Short text about this first point and why it matters.</p>
  <div style="position:absolute;left:140px;top:74px;font-size:8px;color:var(--red)">02</div>
  <div class="head" style="left:156px;top:76px">About Two</div>
  <p class="body" style="left:156px;top:84px;width:124px">Short text about this second point and why it matters.</p>
  <div style="position:absolute;left:140px;top:110px;font-size:8px;color:var(--red)">03</div>
  <div class="head" style="left:156px;top:112px">About Three</div>
  <p class="body" style="left:156px;top:120px;width:124px">Short text about this third point and why it matters.</p>
  <div class="pg">02</div>
</section>

</body>
</html>
```